Zandrix fresh re-design

We are UK based company and have Magento website which we are happy with, but we require fresh design. Menu must be customer friendly

Design must reflect in strength as strength of our products and value for money are our selling points.

Our products are not family products there mainly used for business at events, cycling, running clubs, etc

New design must have same information as current design

links that require new design

http://www.zandrix.example (landing page)

http://www.zandrix.example/3m-x-3m-heavy-duty-tents/3m-x-3m-pop-up-marquee-white.html (product page)

http://www.zandrix.example/custom-design-own-tent-size/choose-3mx3m.html (design tool)

Target Market(s)

business owners, cycling clubs, running clubs,

Industry/Entity Type

It Company

Number of Pages Required

3 page

Requirements
Must have
• background image of working poptent, clean fresh design, printed zandrix eg. cupcake
Should not have
• all same functions as current page

```html
<!DOCTYPE html>
<html lang="en">
<head>
<meta charset="utf-8">
<title>Zandrix – Pop Up Marquees and Gazebos</title>
<link href="https://fonts.googleapis.com/css2?family=Montserrat:wght@400;600;700;800&family=Arvo:wght@700&family=Arimo:wght@400&display=swap" rel="stylesheet">
<style>
:root{
  --navy:#0d1f8c;
  --red:#d9261c;
  --orange:#e8501c;
  --brown:#7a3a1e;
  --text:#333;
  --muted:#555;
  --page:#f7f7f7;
  --footer:#e0e0e0;
  --bar:#8a8a8a;
  --white:#fff;
}
*{margin:0;padding:0;box-sizing:border-box}
html,body{width:941px;height:1200px;overflow:hidden}
body{position:relative;background:var(--page);font-family:Montserrat,sans-serif;color:var(--text)}
.abs{position:absolute}
/* header */
.logo{left:173px;top:16px;display:flex;align-items:center;gap:6px;font-size:17px;font-weight:600;color:var(--navy)}
.logo-mark{width:12px;height:12px;background:var(--red)}
.toplinks{right:162px;top:5px;font-size:7px;color:var(--muted);display:flex;gap:8px}
.nav{left:334px;top:25px;display:flex;gap:0;font-size:8px;font-weight:600}
.nav a{color:var(--text);text-decoration:none;padding:4px 5px;margin-right:22px}
.nav a.active{background:var(--navy);color:var(--white);border-radius:2px;margin-right:16px}
.navrule{left:334px;width:446px;height:1px;background:#ddd}
.cart{right:161px;top:54px;font-size:7px;display:flex;align-items:center;gap:4px}
.cart-count{background:var(--orange);color:var(--white);padding:2px 6px}
/* hero */
.hero{left:0;top:0}
.hero-title{left:162px;top:146px;font-size:35px;font-weight:800;color:var(--white);letter-spacing:.5px}
.hero-sub{left:162px;top:186px;width:320px;font-size:20px;line-height:21.5px;color:var(--white)}
.hero-btn{left:162px;top:262px;width:142px;height:29px;background:var(--orange);color:var(--white);font-size:15px;display:flex;align-items:center;justify-content:center;gap:6px}
/* promo */
.promo-left{left:160px;top:416px;width:430px;height:90px;background:#f1f1f1;border:1px solid #ddd}
.promo-photo{left:160px;top:398px;width:188px;height:108px;background:linear-gradient(90deg,#c0203a 0 50%,#4aa83a 50%)}
.promo-copy{left:399px;top:428px;font-family:Arvo,serif;font-weight:700;color:#222;font-size:15px;line-height:16px}
.promo-copy .red{color:var(--red)}
.promo-price{left:399px;top:466px;font-family:Arvo,serif;font-weight:700;color:var(--navy);font-size:28px}
.promo-price small{font-size:6px;color:var(--red);margin-right:6px}
.promo-right{left:593px;top:416px;width:186px;height:90px;background:var(--navy)}
.why{left:603px;top:421px;font-family:Arvo,serif;font-weight:700;color:var(--white);font-size:16px;line-height:16px}
.why-sub{left:603px;top:457px;font-family:Arvo,serif;font-weight:700;color:var(--white);font-size:8px;line-height:9px}
.why-sub span{color:#f5c400}
.why-tent{left:697px;top:428px;width:75px;height:74px;background:linear-gradient(#e9862c,#c86418)}
.learn{left:603px;top:482px;width:70px;height:20px;background:var(--red);color:var(--white);font-size:7px;font-weight:700;display:flex;align-items:center;justify-content:center}
/* intro */
.intro-title{left:0;width:941px;top:520px;text-align:center;font-size:12.5px;color:var(--muted)}
.intro-text{left:160px;top:544px;width:620px;font-family:Arimo,sans-serif;font-size:7px;line-height:14.4px;color:#333}
.divider{left:161px;top:621px;width:618px;height:5px;background:#e6e6e6}
/* services */
.services-title{left:0;width:941px;top:645px;text-align:center;font-size:20px;color:var(--brown)}
.services-text{left:190px;width:561px;top:673px;text-align:center;font-size:9px;line-height:11px;color:var(--muted)}
.card{top:719px;width:143px;height:184px;background:var(--white);box-shadow:0 0 2px rgba(0,0,0,.12)}
.card-img{width:143px;height:134px}
.card-text{padding:6px 6px;font-size:8px;line-height:14.5px;color:var(--text)}
.arrow{top:791px;width:14px;height:32px;background:#e4e4e4;display:flex;align-items:center;justify-content:center}
/* partners */
.partners{left:161px;top:923px;width:618px;height:65px;background:var(--white)}
.partners-title{left:183px;top:942px;font-size:19px;color:var(--brown)}
.badge{top:936px;height:40px}
/* footer */
.footer{left:0;top:1010px;width:941px;height:155px;background:var(--footer)}
.fcol{top:1021px;font-size:8px;color:var(--muted);line-height:14.4px}
.fcol h4{font-size:10px;font-weight:600;color:#333;margin-bottom:6px}
.social li{list-style:none;display:flex;align-items:center;gap:6px;margin-left:-2px}
.social i{display:inline-block;width:11px;height:11px;background:#555}
.seal{left:676px;top:1020px;width:85px;height:37px;background:var(--white);border-bottom:6px solid #2e8b3a;border-radius:3px}
.bottombar{left:0;top:1165px;width:941px;height:35px;background:var(--bar);color:var(--white);font-size:8px;padding:13px 153px}
</style>
</head>
<body>

<svg class="abs hero" width="941" height="400" viewBox="0 0 941 400" role="img" aria-label="Evening campsite with folding chairs around a fire and lanterns at sunset">
  <defs>
    <linearGradient id="heroSky" x1="0" y1="0" x2="0" y2="1">
      <stop offset="0" stop-color="#6e5a52"/>
      <stop offset=".35" stop-color="#b0643a"/>
      <stop offset=".6" stop-color="#4d5a2e"/>
      <stop offset="1" stop-color="#8a7a64"/>
    </linearGradient>
  </defs>
  <polygon points="0,96 264,62 941,86 941,340 520,385 0,340" fill="url(#heroSky)"/>
</svg>

<div class="abs logo"><span class="logo-mark"></span>zandrix</div>
<div class="abs toplinks"><span>My Account</span><span>Sign In</span><span>View Cart</span></div>
<div class="abs navrule" style="top:19px"></div>
<nav class="abs nav">
  <a class="active">Zandrix</a><a>Roofs walls</a><a>Gazebo</a><a>Weights</a><a>Gutters</a><a>Sandbags</a><a>Tables</a><a style="margin-right:0">Parts</a>
</nav>
<div class="abs navrule" style="top:48px"></div>
<div class="abs cart">
  <svg width="14" height="9" viewBox="0 0 14 9"><path d="M0 1h3l2 5h7l1-4H4" fill="none" stroke="#222" stroke-width="1.2"/><circle cx="6" cy="8" r="1" fill="#222"/><circle cx="11" cy="8" r="1" fill="#222"/></svg>
  <span>Your Cart</span><span class="cart-count">0 Item</span><span>$0.00</span>
</div>

<h1 class="abs hero-title">THE GOOD FEELING</h1>
<p class="abs hero-sub">Outdoor specialize in providing you an optimal outdoor experience</p>
<div class="abs hero-btn">Product Store
  <svg width="13" height="13" viewBox="0 0 13 13"><circle cx="6.5" cy="6.5" r="6.5" fill="#fff"/><path d="M5 3.5l3 3-3 3" fill="none" stroke="#e8501c" stroke-width="1.8"/></svg>
</div>

<div class="abs promo-left"></div>
<div class="abs promo-photo" role="img" aria-label="Two printed branded pop-up tents in red and green"></div>
<div class="abs promo-copy">DESIGN <span style="font-size:12px">your own</span><br><span class="red">ZANDRIX</span></div>
<div class="abs promo-price"><small>FROM</small>€490</div>
<div class="abs promo-right"></div>
<div class="abs why-tent" role="img" aria-label="Orange pop-up gazebo"></div>
<div class="abs why">WHY BUY<br>from us?</div>
<div class="abs why-sub">Zandrix provide<br>the <span>Cheapest prices</span></div>
<div class="abs learn">LEARN MORE</div>

<h2 class="abs intro-title" style="font-weight:400">Pop Up Marquees and Gazebos for Sale</h2>
<p class="abs intro-text">Mini Pop Up Marquess and Gazebos with sides<br>Pop up marquees / heavy duty gazebo for sale near you! We at zandrix have been able to expand our markets to different countries and our pop up marquees and heavy duty gazebos are now available for delivery in several European countries, so your wait is over. All you have to do now is order your instant awnings from our website zandrix.example Please note we deliver to Ireland and all over Europe.</p>
<div class="abs divider"></div>

<h2 class="abs services-title" style="font-weight:400">Our Services</h2>
<p class="abs services-text">Lorem Ipsum is simply dummy text of the printing and typesetting industry. Lorem Ipsum has been the industry's standard dummy text ever since the 1500s, when an unknown printer took a galley of type and scrambled it to make a type specimen book.</p>

<div class="abs arrow" style="left:140px"><svg width="6" height="9"><path d="M5 1L1 4.5 5 8" fill="none" stroke="#666" stroke-width="1.2"/></svg></div>
<div class="abs card" style="left:161px"><div class="card-img" role="img" aria-label="White 3m by 3m heavy duty pop-up tent" style="background:linear-gradient(#5a6a4a,#e6e8e4 55%,#fff)"></div><div class="card-text">3m x 3m Heavy Duty Pop-Up<br>White<br>€449.00 ex vat</div></div>
<div class="abs card" style="left:319px"><div class="card-img" role="img" aria-label="Yellow 15kg metal weight on a tent leg" style="background:linear-gradient(#4f6a3a,#8a9a5a 50%,#f0f0ea)"></div><div class="card-text">15kg Metal Weights<br>€65.00 ex vat</div></div>
<div class="abs card" style="left:477px"><div class="card-img" role="img" aria-label="Orange 3m by 3m heavy duty pop-up tent" style="background:linear-gradient(#4a5a3a,#e07a20 45%,#f4ece4 90%)"></div><div class="card-text">3m x 3m Heavy Duty Pop-Up<br>White<br>€449.00 ex vat</div></div>
<div class="abs card" style="left:635px"><div class="card-img" role="img" aria-label="White pop-up tent with side walls on grass" style="background:linear-gradient(#5a6a5a,#e8eaea 45%,#fff)"></div><div class="card-text">3m x 3m Heavy Duty Pop-Up<br>White<br>€449.00 ex vat</div></div>
<div class="abs arrow" style="left:787px"><svg width="6" height="9"><path d="M1 1l4 3.5L1 8" fill="none" stroke="#666" stroke-width="1.2"/></svg></div>

<div class="abs partners"></div>
<h3 class="abs partners-title" style="font-weight:400">Our Partner’s</h3>
<div class="abs badge" style="left:329px;top:936px;width:60px;background:var(--red)" role="img" aria-label="Norvane partner badge"></div>
<div class="abs badge" style="left:403px;top:936px;width:126px;background:var(--red);border-radius:6px" role="img" aria-label="Campford partner badge"></div>
<div class="abs badge" style="left:553px;top:940px;width:202px;height:31px;background:#12a6dc" role="img" aria-label="Coolhaven partner badge"></div>

<footer class="abs footer"></footer>
<div class="abs fcol" style="left:150px"><h4>Information</h4>About Us<br>FAQ<br>Instuctions<br>Contact us<br>Delivery, Payments and Returns<br>Blog<br>Log In</div>
<div class="abs fcol" style="left:355px"><h4>Our Services</h4>Printed Zandrix<br>Tenders<br>Tent Templates</div>
<div class="abs fcol" style="left:512px"><h4>Connect With Us</h4>
  <ul class="social"><li><i></i>Linkpage</li><li><i></i>Chirpline</li><li><i></i>Circleplus</li><li><i></i>Vidstream</li></ul>
</div>
<div class="abs seal" role="img" aria-label="Securetrust certification seal"></div>
<div class="abs bottombar">© 2014 Zandrix TM. All Rights Reserved.</div>

</body>
</html>
```